Business Card Design - Law Firm

We are a boutique law firm located near the beach in Manly, Australia. We have recently had a new logo designed and are revamping our business cards with the new logo.

We have recently had a business card design done for us but are not entirely happy with it. We are looking for something modern, simplistic but striking. We would like to see multiple designs.

We have attached a word document which includes our new logo and the current business card design which we are looking at moving away from.

We would like the business cards to be double sided. We would like the design to include something which we can print in gloss colour when we send it to the business card printers.

```html
<!DOCTYPE html>
<html lang="en">
<head>
<meta charset="utf-8">
<title>Harlow &amp; Partners – Business Card</title>
<link rel="stylesheet" href="https://fonts.googleapis.com/css2?family=Montserrat:wght@600&family=Arimo:wght@400&display=swap">
<style>
  :root {
    --backdrop: #e4e4e4;
    --card: #f6f5f3;
    --ink: #1f1f1f;
    --accent: #3f4aa8;
    --icon: #4a55b0;
  }
  * { margin: 0; padding: 0; box-sizing: border-box; }
  html, body {
    width: 1200px; height: 880px; overflow: hidden;
    background: var(--backdrop);
  }
  .canvas { position: relative; width: 1200px; height: 880px; }
  .card {
    position: absolute; left: 390px; width: 421px; height: 240px;
    background: var(--card);
    box-shadow: 0 1px 3px rgba(0,0,0,0.12);
  }
  .card--front { top: 180px; }
  .card--back { top: 449px; }

  .brand {
    position: absolute; display: flex; align-items: center; gap: 10px;
    font-family: "Montserrat", sans-serif; font-weight: 600;
    color: var(--ink); letter-spacing: 0.08em; white-space: nowrap;
  }
  .brand__dot { border-radius: 50%; background: var(--accent); flex: none; }
  .card--front .brand {
    left: 50%; top: 50%; transform: translate(-50%, -50%); font-size: 20px;
  }
  .card--front .brand__dot { width: 18px; height: 18px; }
  .card--back .brand {
    left: 90px; top: 123px; transform: translate(-50%, -50%); font-size: 10.5px; gap: 6px;
  }
  .card--back .brand__dot { width: 10px; height: 10px; }

  .person {
    position: absolute; left: 192px; top: 46px;
    font-family: "Arimo", sans-serif;
  }
  .person__name { font-size: 21px; color: var(--ink); font-weight: 400; line-height: 1.2; }
  .person__role { font-size: 12.5px; color: var(--accent); margin-top: 2px; }

  .contact {
    position: absolute; left: 192px; top: 118px; list-style: none;
    font-family: "Arimo", sans-serif; font-size: 12px; color: var(--ink); line-height: 14.5px;
  }
  .contact__item { display: flex; align-items: flex-start; gap: 8px; }
  .contact__icon { width: 12px; height: 12px; margin-top: 1px; flex: none; }
  .contact__text--indent { padding-left: 20px; }
</style>
</head>
<body>
<main class="canvas">
  <section class="card card--front" aria-label="Card front">
    <div class="brand"><span class="brand__dot"></span>Harlow &amp; Partners</div>
  </section>

  <section class="card card--back" aria-label="Card back">
    <div class="brand"><span class="brand__dot"></span>Harlow &amp; Partners</div>

    <div class="person">
      <h1 class="person__name">Megan Ellis</h1>
      <p class="person__role">Practice Manager</p>
    </div>

    <ul class="contact">
      <li class="contact__item">
        <svg class="contact__icon" viewBox="0 0 12 12"><circle cx="6" cy="6" r="6" fill="var(--icon)"/><path d="M4 3.2l1 1.3-.6.7c.4.9 1 1.5 1.9 1.9l.7-.6 1.3 1-.6 1C5.8 8.3 3.7 6.2 3.5 3.8z" fill="#fff"/></svg>
        <span>(02) 9000 4187</span>
      </li>
      <li class="contact__item">
        <svg class="contact__icon" viewBox="0 0 12 12"><circle cx="6" cy="6" r="6" fill="var(--icon)"/><rect x="3" y="4" width="6" height="4.2" fill="#fff"/><path d="M3 4l3 2.2L9 4" stroke="var(--icon)" stroke-width=".7" fill="none"/></svg>
        <span>megan.ellis@harlowlaw.com.au</span>
      </li>
      <li class="contact__item">
        <svg class="contact__icon" viewBox="0 0 12 12"><circle cx="6" cy="6" r="6" fill="var(--icon)"/><g stroke="#fff" stroke-width=".6" fill="none"><circle cx="6" cy="6" r="3"/><ellipse cx="6" cy="6" rx="1.3" ry="3"/><path d="M3 6h6"/></g></svg>
        <span>harlowandpartners.com.au</span>
      </li>
      <li class="contact__item">
        <svg class="contact__icon" viewBox="0 0 12 12"><circle cx="6" cy="6" r="6" fill="var(--icon)"/><path d="M6 2.6a2.3 2.3 0 0 1 2.3 2.3C8.3 6.6 6 9.3 6 9.3S3.7 6.6 3.7 4.9A2.3 2.3 0 0 1 6 2.6z" fill="#fff"/><circle cx="6" cy="4.9" r=".9" fill="var(--icon)"/></svg>
        <span>Suite 4, 12 Tidewater Lane</span>
      </li>
      <li class="contact__item contact__text--indent">COVEHAVEN NSW 2199</li>
    </ul>
  </section>
</main>
</body>
</html>
```